LV Business Card NEEDED

Larch Vantage is a finance brokering company that provide lending advise to consumer, business, corporate, and property developer for all their financing needs.

We source and match customer needs in Home Loan, Business Loan, Commercial Property Loan, Assets Finance, and other banking related services. It is a market with full of loans! But we specialise in more complex loan structure and our client base are more business and corporate level. Our suppliers are Banks and large Financial Institution where these business card will go to.

We have a great deal of Asian clients, therefore the card need to also include Chinese language together with English.

Refer to attached file for logo and content requirements.

We are looking for designs with the following ingredients:
* Innovative & Creative
* Professional
* Trust & Security

Please pick colours that will compliment the colours of the company logo.

Please provide a unique design, for example the edge of the card is rounded or corner cut off.

Company logo uploaded.

Please commence submitting your design.

Target Market(s)

Target audiences are businessmen, corporate, and property developer. And also a great deal of Chinese clients.

Industry/Entity Type

Finance

Contact Information for Business Card

Larch Vantage Pty. Ltd.
Morris Pelham
Director
Suite 27, 3-9 Quenby St. Auburn NSW 2144

Requirements
Must have
• Double sided design

```html
<!DOCTYPE html>
<html lang="en">
<head>
<meta charset="utf-8">
<title>Larch Vantage – Business Card Colour Options</title>
<link rel="stylesheet" href="https://fonts.googleapis.com/css2?family=Arimo:wght@400;700&family=Noto+Serif+TC:wght@600&display=swap">
<style>
  :root {
    --backdrop: #a6a6a6;
    --sheet: #ffffff;
    --card: #ffffff;
    --card-edge: #d8d8d8;
    --shadow: rgba(0, 0, 0, 0.28);
    --ink: #222222;
    --grey-bar: #a9a9a9;
    --grey-text: #6d6d6d;
    --bullet: #808080;
    --mark: #9a9a9a;
    --logo-ink: #3a3a3a;
    --green: #7fc31c;
    --red: #e2231a;
    --orange: #e8791a;
    --yellow: #f4c200;
  }
  * { box-sizing: border-box; margin: 0; padding: 0; }
  html, body { width: 1200px; height: 928px; overflow: hidden; }
  body {
    background: var(--backdrop);
    font-family: "Arimo", Arial, sans-serif;
    position: relative;
  }
  .sheet {
    position: absolute;
    left: 80px; top: 61px;
    width: 1041px; height: 805px;
    background: var(--sheet);
    box-shadow: -14px 16px 18px rgba(0,0,0,0.25);
  }
  .option { position: absolute; width: 385px; }
  .option--tl { left: 97px;  top: 96px; }
  .option--tr { left: 567px; top: 96px; }
  .option--bl { left: 97px;  top: 438px; }
  .option--br { left: 567px; top: 438px; }

  .card {
    position: relative;
    width: 385px; height: 236px;
    background: var(--card);
    border: 1px solid var(--card-edge);
    box-shadow: -12px 12px 10px var(--shadow);
    overflow: hidden;
  }
  .brand {
    position: absolute; left: 0; right: 0; top: 16px;
    text-align: center;
  }
  .brand__dot {
    display: block;
    width: 48px; height: 48px; margin: 0 auto;
    border-radius: 50%;
    background: var(--mark);
  }
  .brand__name {
    display: block;
    margin-top: 11px;
    font-size: 9px;
    letter-spacing: 5.2px;
    color: var(--logo-ink);
    line-height: 10px;
  }
  .brand__chinese {
    display: inline-block;
    font-family: "Noto Serif TC", serif;
    font-size: 12px;
    line-height: 13px;
    color: var(--logo-ink);
    padding-bottom: 2px;
    border-bottom: 1px solid #cfcfcf;
    width: 142px;
  }
  .title-bar {
    position: absolute; left: 0; right: 0; top: 124px; height: 14px;
    display: flex; align-items: center;
  }
  .title-bar__rule { height: 14px; background: var(--grey-bar); }
  .title-bar__rule--long { width: 168px; }
  .title-bar__rule--short { flex: 1; }
  .title-bar__text {
    padding: 0 5px;
    font-size: 12px;
    color: var(--grey-text);
    white-space: nowrap;
  }
  .services {
    position: absolute; left: 0; right: 0; top: 154px;
    list-style: none;
    font-size: 12px;
    color: var(--grey-text);
    text-align: center;
    line-height: 21px;
  }
  .services__row { display: block; }
  .services__item { display: inline-block; margin: 0 5px; }
  .services__item::before {
    content: "";
    display: inline-block;
    width: 7px; height: 7px;
    border-radius: 50%;
    background: var(--bullet);
    margin-right: 6px;
    vertical-align: 1px;
  }
  .office {
    position: absolute; left: 0; right: 0; bottom: 0; height: 25px;
    background: var(--accent);
    color: #ffffff;
    font-size: 11.5px;
    line-height: 25px;
    text-align: center;
    white-space: nowrap;
  }
  .office strong { font-weight: 700; }

  .caption {
    position: relative; height: 30px; margin-top: 22px;
    font-size: 16px; color: var(--ink);
  }
  .caption__size { position: absolute; left: 14px; top: 6px; }
  .caption__colour { position: absolute; right: 34px; top: 6px; font-weight: 700; }
  .option--bl .caption__size { top: 12px; }
  .option--br .caption__size { left: 50px; top: 12px; }
  .option--bl .caption__colour, .option--br .caption__colour { top: 8px; }
  .option--tr .caption__colour { right: 20px; }
  .option--br .caption__colour { right: 0; }
  .option--bl .caption__colour { right: 8px; }

  .accent-green  { --accent: var(--green); }
  .accent-red    { --accent: var(--red); }
  .accent-orange { --accent: var(--orange); }
  .accent-yellow { --accent: var(--yellow); }
</style>
</head>
<body>
<main class="sheet">

  <section class="option option--tl accent-green">
    <div class="card">
      <div class="brand">
        <span class="brand__dot"></span>
        <span class="brand__name">LARCH VANTAGE</span>
        <span class="brand__chinese">嘉橡匯</span>
      </div>
      <div class="title-bar"><span class="title-bar__rule title-bar__rule--long"></span><span class="title-bar__text">DIRECTOR - MORRIS PELHAM</span><span class="title-bar__rule title-bar__rule--short"></span></div>
      <ul class="services">
        <li class="services__row"><span class="services__item">Home Loan</span><span class="services__item">Business Loan</span><span class="services__item">Assets Finance</span></li>
        <li class="services__row"><span class="services__item">Banking Services</span><span class="services__item">Commercial Property Loan</span></li>
      </ul>
      <p class="office"><strong>Office :</strong> Suite 27, 3-9 Quenby St. Brindle Vale NSW 2911</p>
    </div>
    <div class="caption"><span class="caption__size">9.5 cm x 5 cm</span><span class="caption__colour">Green Colour</span></div>
  </section>

  <section class="option option--tr accent-red">
    <div class="card">
      <div class="brand">
        <span class="brand__dot"></span>
        <span class="brand__name">LARCH VANTAGE</span>
        <span class="brand__chinese">嘉橡匯</span>
      </div>
      <div class="title-bar"><span class="title-bar__rule title-bar__rule--long"></span><span class="title-bar__text">DIRECTOR - MORRIS PELHAM</span><span class="title-bar__rule title-bar__rule--short"></span></div>
      <ul class="services">
        <li class="services__row"><span class="services__item">Home Loan</span><span class="services__item">Business Loan</span><span class="services__item">Assets Finance</span></li>
        <li class="services__row"><span class="services__item">Banking Services</span><span class="services__item">Commercial Property Loan</span></li>
      </ul>
      <p class="office"><strong>Office :</strong> Suite 27, 3-9 Quenby St. Brindle Vale NSW 2911</p>
    </div>
    <div class="caption"><span class="caption__size">9.5 cm x 5 cm</span><span class="caption__colour">Red Colour</span></div>
  </section>

  <section class="option option--bl accent-orange">
    <div class="card">
      <div class="brand">
        <span class="brand__dot"></span>
        <span class="brand__name">LARCH VANTAGE</span>
        <span class="brand__chinese">嘉橡匯</span>
      </div>
      <div class="title-bar"><span class="title-bar__rule title-bar__rule--long"></span><span class="title-bar__text">DIRECTOR - MORRIS PELHAM</span><span class="title-bar__rule title-bar__rule--short"></span></div>
      <ul class="services">
        <li class="services__row"><span class="services__item">Home Loan</span><span class="services__item">Business Loan</span><span class="services__item">Assets Finance</span></li>
        <li class="services__row"><span class="services__item">Banking Services</span><span class="services__item">Commercial Property Loan</span></li>
      </ul>
      <p class="office"><strong>Office :</strong> Suite 27, 3-9 Quenby St. Brindle Vale NSW 2911</p>
    </div>
    <div class="caption"><span class="caption__size">9.5 cm x 5 cm</span><span class="caption__colour">Orange Sunkiss Colour</span></div>
  </section>

  <section class="option option--br accent-yellow">
    <div class="card">
      <div class="brand">
        <span class="brand__dot"></span>
        <span class="brand__name">LARCH VANTAGE</span>
        <span class="brand__chinese">嘉橡匯</span>
      </div>
      <div class="title-bar"><span class="title-bar__rule title-bar__rule--long"></span><span class="title-bar__text">DIRECTOR - MORRIS PELHAM</span><span class="title-bar__rule title-bar__rule--short"></span></div>
      <ul class="services">
        <li class="services__row"><span class="services__item">Home Loan</span><span class="services__item">Business Loan</span><span class="services__item">Assets Finance</span></li>
        <li class="services__row"><span class="services__item">Banking Services</span><span class="services__item">Commercial Property Loan</span></li>
      </ul>
      <p class="office"><strong>Office :</strong> Suite 27, 3-9 Quenby St. Brindle Vale NSW 2911</p>
    </div>
    <div class="caption"><span class="caption__size">9.5 cm x 5 cm</span><span class="caption__colour">Yellow Colour</span></div>
  </section>

</main>
</body>
</html>
```